SPICE LABEL DESIGN FOR A TASTY DRY RUB! (chicken, ribs, wings)

Looking for a fun/creative/edgy label for a spice jar! The label will be rectangular (exact size tbd - but approximately 1.2" W X 3" H).
This spice is a dry rub blend of 14 EPIC spices, to be used on chicken, chicken wings, ribs, etc.
Copywritting on the label to be;
Tova JK's Blaze BBQ Rub
A blend of 14 UNTOVAGETTABLE spices
*Note the word "untovagettabe" is spelt incorectly on purpose for a play a words with "tova". Please use a different color font for "tova" within the word.
Also would like "Tova JK's" to be prominent
Looking for an illustration/design that is fun/creative/catchy/edgy/appealing! While still keeping the design appealing to higher end markets. Have fun with it and think outside of the box!! :)
People who enjoy cooking, young adults and adults, display at restaurants or retail markets

```html
<!DOCTYPE html>
<html lang="en">
<head>
<meta charset="utf-8">
<title>Tova JK's Blaze BBQ Rub – Label</title>
<link rel="stylesheet" href="https://fonts.googleapis.com/css2?family=Alfa+Slab+One&family=Oswald:wght@600&family=Montserrat:wght@500;600&display=swap">
<style>
  :root {
    --backdrop: #fad0a9;
    --label-white: #ffffff;
    --teal: #40bcb9;
    --maroon: #8a1a2b;
    --slate: #6b6b70;
    --blush: #ecc9ca;
    --hen-white: #f4f1ea;
  }
  * { margin: 0; padding: 0; box-sizing: border-box; }
  html, body {
    width: 961px; height: 1200px; overflow: hidden;
    background: var(--backdrop);
  }
  .label {
    position: absolute; left: 301px; top: 149px;
    width: 358px; height: 899px;
    background: var(--label-white);
    overflow: hidden;
  }
  .deco { position: absolute; background: var(--blush); opacity: .55; }
  .deco--tomato-top { left: 2px; top: 30px; width: 74px; height: 74px; border-radius: 50%; }
  .deco--pepper-top { left: 262px; top: 72px; width: 110px; height: 40px; border-radius: 40px 0 0 40px; }
  .deco--chili { left: 0; top: 724px; width: 38px; height: 160px; border-radius: 0 20px 20px 0; }
  .deco--tomato-bottom { left: 304px; top: 759px; width: 92px; height: 100px; border-radius: 50%; }

  .brand-plate {
    position: absolute; left: 59px; top: 0; width: 240px; height: 105px;
    border: 2px solid var(--teal); border-top: none;
  }
  .brand-plate__fill {
    position: absolute; left: 8px; top: 0; right: 8px; bottom: 8px;
    background: var(--teal);
    display: flex; align-items: center; justify-content: center;
  }
  .brand-name {
    font-family: "Alfa Slab One", serif; font-weight: 400;
    font-size: 33px; color: var(--label-white); letter-spacing: 0.5px;
    white-space: nowrap;
  }
  .product-kicker {
    position: absolute; left: 0; width: 100%; top: 150px;
    text-align: center;
    font-family: "Alfa Slab One", serif; font-size: 40px; line-height: 50px;
    color: var(--slate); letter-spacing: 1px;
  }
  .product-title {
    position: absolute; left: 0; width: 100%;
    text-align: center;
    font-family: "Alfa Slab One", serif; font-size: 118px; line-height: 1;
    color: var(--maroon); letter-spacing: 1px;
  }
  .product-title--bbq { top: 186px; }
  .product-title--rub { top: 300px; }
  .tools-rule {
    position: absolute; left: 67px; top: 263px; width: 224px; height: 66px;
    overflow: visible;
  }
  .mascot {
    position: absolute; left: 75px; top: 444px; width: 208px; height: 208px;
    border-radius: 50%;
    background: radial-gradient(circle, var(--hen-white) 0 45%, var(--teal) 75%);
  }
  .blend-bar {
    position: absolute; left: 37px; top: 681px; width: 277px; height: 28px;
    background: var(--teal);
    display: flex; align-items: center; justify-content: center;
    font-family: "Montserrat", sans-serif; font-weight: 600;
    font-size: 17px; letter-spacing: 4px; color: var(--label-white);
  }
  .spice-count {
    position: absolute; left: 0; width: 100%; top: 716px;
    text-align: center;
    font-family: "Alfa Slab One", serif; font-size: 60px; line-height: 70px;
    color: var(--maroon);
  }
  .spice-word {
    position: absolute; left: 0; width: 100%; top: 782px;
    text-align: center; white-space: nowrap;
    font-family: "Oswald", sans-serif; font-weight: 600;
    font-size: 42px; line-height: 50px; letter-spacing: -1.5px;
    color: var(--slate);
  }
  .spice-word__name { color: var(--maroon); }
  .spice-label {
    position: absolute; left: 0; width: 100%; top: 834px;
    text-align: center;
    font-family: "Montserrat", sans-serif; font-weight: 500;
    font-size: 17px; letter-spacing: 4px; color: var(--slate);
  }
  .footer-band {
    position: absolute; left: 0; bottom: 0; width: 100%; height: 30px;
    background: var(--teal);
  }
</style>
</head>
<body>
  <main class="label">
    <div class="deco deco--tomato-top" role="img" aria-label="Faint sliced tomato illustration"></div>
    <div class="deco deco--pepper-top" role="img" aria-label="Faint sliced pepper illustration"></div>
    <div class="deco deco--chili" role="img" aria-label="Faint chili pepper illustration"></div>
    <div class="deco deco--tomato-bottom" role="img" aria-label="Faint sliced tomato illustration"></div>

    <header class="brand-plate">
      <div class="brand-plate__fill"><span class="brand-name">TOVA JK'S</span></div>
    </header>

    <p class="product-kicker">BLAZE</p>
    <h1 class="product-title product-title--bbq">BBQ</h1>
    <h1 class="product-title product-title--rub">RUB</h1>
    <svg class="tools-rule" viewBox="0 0 224 66" aria-hidden="true">
      <g stroke="#40bcb9" fill="none" stroke-linecap="round">
        <line x1="0" y1="36" x2="64" y2="36" stroke-width="3" stroke-linecap="butt"/>
        <line x1="160" y1="36" x2="224" y2="36" stroke-width="3" stroke-linecap="butt"/>
        <!-- spatula -->
        <line x1="99" y1="18" x2="122" y2="62" stroke-width="4"/>
        <!-- fork -->
        <line x1="134" y1="14" x2="86" y2="62" stroke-width="4"/>
        <path d="M134 14 L140 4 M131 11 L134 2 M137 17 L146 10" stroke-width="2.5"/>
      </g>
      <rect x="88" y="2" width="16" height="18" rx="2" fill="#40bcb9" transform="rotate(-28 96 11)"/>
      <g stroke="#ffffff" stroke-width="1.5">
        <line x1="93" y1="6" x2="96" y2="16" transform="rotate(-28 96 11)"/>
        <line x1="99" y1="6" x2="99" y2="16" transform="rotate(-28 96 11)"/>
      </g>
    </svg>

    <div class="mascot" role="img" aria-label="Cartoon rooster mascot giving an OK sign in front of a teal circle"></div>

    <div class="blend-bar">A BLEND OF</div>
    <p class="spice-count">14</p>
    <p class="spice-word">UN<span class="spice-word__name">TOVA</span>GETTABLE</p>
    <p class="spice-label">SPICES</p>

    <div class="footer-band"></div>
  </main>
</body>
</html>
```